Business Card for Language School (2 locations)

We need a sleek business card for a language school that is looking to update our image to be more professional. We work with students ages Pre-Kindergarten through adults. Our idea is to have an all-black business card with white or silver lettering. On the front will be the name of our school (Bright Maple English Academy), and on the back there will be information for our location, phone number, email, and website (and possibly social media information). We have two school branches, so the address, phone number, and email address will be different for each branch, but all of the other information will stay the same. We'd like each branch to have a different color card edge that is neon. We are also open to suggestions and new ideas!

Some answers to questions we have received:
1. The reason we haven't added a logo is because we are looking to get a new one. We hadn't originally planned to do that at this time, but we are going to look into updating our project to include that as another aspect of it. We had previously planned to just include the school name on the front without a logo at this time.
2. We currently have two branches of our school, and we want our business card design to be uniform for each location. While it might make sense to put the information on one card right now, we plan to have more locations in the future, so we want to plan ahead with a unified design right now.
3. Our school addresses and phone numbers can be found on our website: www.brightmapleenglish.example (at the bottom of the page)!
Updates

Part of this contest is also a new logo design. Our previous design was a train, which we would be open to keeping if it had an updated, sleeker design.

Contact Information for Business Card

Card #1:
Bright Maple English Academy (Qiaolin Branch)
Yuqing W. Rd. Sec. 3, Lane 412, No. 29, 1F
Beitou District, Taipei City 11268
02-2649-3058
qiaolin@brightmapleenglish.example

Card #2:
Bright Maple English Academy (Fenghe Branch)
Fulan Road, No. 318, 1F
Songshan District, Taipei City 10573
02-2761-4402
fenghe@brightmapleenglish.example

Both cards:
Website: www.brightmapleenglish.example
Facebook: www.facebook.com/brightmapleenglish
Instagram: @brightmapleenglish

```html
<!DOCTYPE html>
<html lang="en">
<head>
<meta charset="utf-8">
<title>Bright Maple English Academy — Qiaolin Branch Business Card</title>
<link rel="stylesheet" href="https://fonts.googleapis.com/css2?family=Saira+Condensed:wght@500&display=swap">
<style>
  :root {
    --page-bg: #2b2f36;
    --card-dark: #141414;
    --card-mid: #232323;
    --text-light: #f2f2f2;
    --accent-red: #e5443d;
    --icon-bg: #ffffff;
  }
  * { margin: 0; padding: 0; box-sizing: border-box; }
  html, body {
    width: 1200px;
    height: 802px;
    overflow: hidden;
    background: var(--page-bg);
  }
  .business-card {
    position: absolute;
    left: 90px;
    top: 86px;
    width: 1020px;
    height: 630px;
    background: linear-gradient(180deg, var(--card-mid) 0%, var(--card-dark) 100%);
    font-family: "Saira Condensed", "Arial Narrow", sans-serif;
    font-weight: 500;
    color: var(--text-light);
    overflow: hidden;
    box-shadow: 0 18px 40px rgba(0,0,0,0.45);
  }
  .card-shapes { position: absolute; inset: 0; }
  .school-name, .branch-name {
    position: absolute;
    right: 40px;
    font-size: 44px;
    line-height: 56px;
    text-align: right;
    white-space: nowrap;
  }
  .school-name { top: 40px; }
  .branch-name { top: 104px; color: var(--accent-red); }
  .text-line {
    position: absolute;
    height: 40px;
    line-height: 40px;
    font-size: 32px;
    white-space: nowrap;
  }
  .left-text { left: 88px; }
  .left-text.small { font-size: 30px; }
  .contact-icon {
    position: absolute;
    left: 30px;
    width: 40px;
    height: 40px;
  }
  .social-text { left: 724px; }
  .social-mark {
    position: absolute;
    left: 672px;
    width: 36px;
    height: 36px;
    background: var(--icon-bg);
    border-radius: 50%;
  }
  .social-mark.square { border-radius: 8px; }
</style>
</head>
<body>
  <div class="business-card">
    <svg class="card-shapes" width="1020" height="630" viewBox="0 0 1020 630">
      <defs>
        <linearGradient id="edge-glow" x1="0" y1="0" x2="0" y2="1">
          <stop offset="0" stop-color="#ffffff"/>
          <stop offset="0.45" stop-color="#ffffff"/>
          <stop offset="0.72" stop-color="#e5443d"/>
          <stop offset="0.9" stop-color="#f6c9c6"/>
          <stop offset="1" stop-color="#ffffff"/>
        </linearGradient>
        <linearGradient id="right-panel-tone" x1="0" y1="0" x2="1" y2="1">
          <stop offset="0" stop-color="#262626"/>
          <stop offset="1" stop-color="#181818"/>
        </linearGradient>
      </defs>
      <polygon points="444,0 1020,0 1020,630 614,630" fill="url(#right-panel-tone)" role="img" aria-label="Subtle interlocking geometric texture panel"/>
      <polygon points="438,0 446,0 616,630 608,630" fill="url(#edge-glow)"/>
    </svg>

    <div class="school-name">Bright Maple English Academy</div>
    <div class="branch-name">(Qiaolin Branch)</div>

    <svg class="contact-icon" style="top:192px" viewBox="0 0 40 40" aria-hidden="true">
      <circle cx="20" cy="20" r="20" fill="#ffffff"/>
      <path d="M13 11 l5 0 2 6 -3 2 c1.5 3 3 4.5 6 6 l2 -3 6 2 0 5 c-10 1 -19 -8 -18 -18z" fill="#e5443d"/>
    </svg>
    <div class="text-line left-text" style="top:192px">02-2649-3058</div>

    <svg class="contact-icon" style="top:261px" viewBox="0 0 40 40" aria-hidden="true">
      <circle cx="20" cy="20" r="20" fill="#ffffff"/>
      <path d="M20 9 c-5 0 -8 3.5 -8 8 c0 6 8 14 8 14 s8 -8 8 -14 c0 -4.5 -3 -8 -8 -8z" fill="#e5443d"/>
      <circle cx="20" cy="17" r="3" fill="#ffffff"/>
    </svg>
    <div class="text-line left-text" style="top:261px">Yuqing W. Rd. Sec. 3,</div>
    <div class="text-line left-text" style="top:325px">Lane 412, No. 29, 1F</div>
    <div class="text-line left-text" style="top:388px">Beitou District, Taipei City 11268</div>

    <svg class="contact-icon" style="top:453px" viewBox="0 0 40 40" aria-hidden="true">
      <circle cx="20" cy="20" r="20" fill="#ffffff"/>
      <rect x="10" y="13" width="20" height="14" rx="1.5" fill="#e5443d"/>
      <path d="M10.5 14 l9.5 7.5 9.5 -7.5" fill="none" stroke="#ffffff" stroke-width="1.8"/>
    </svg>
    <div class="text-line left-text small" style="top:453px">qiaolin@brightmapleenglish.example</div>

    <svg class="contact-icon" style="top:527px" viewBox="0 0 40 40" aria-hidden="true">
      <circle cx="20" cy="20" r="20" fill="#ffffff"/>
      <circle cx="20" cy="20" r="10" fill="none" stroke="#e5443d" stroke-width="2.4"/>
      <ellipse cx="20" cy="20" rx="4.5" ry="10" fill="none" stroke="#e5443d" stroke-width="2"/>
      <line x1="10" y1="20" x2="30" y2="20" stroke="#e5443d" stroke-width="2"/>
    </svg>
    <div class="text-line left-text small" style="top:527px">www.brightmapleenglish.example</div>

    <span class="social-mark" style="top:394px"></span>
    <div class="text-line social-text" style="top:392px">www.social.example/</div>
    <div class="text-line social-text" style="top:453px">brightmapleenglish</div>

    <span class="social-mark square" style="top:529px"></span>
    <div class="text-line social-text" style="top:527px">@brightmapleenglish</div>
  </div>
</body>
</html>
```